Redesign Tilda's RV Park & Lodge Website, Leeds, North Dakota

I need a totally re-designed website for my RV Park / Lodge. I want to not only provide information on my RV Park / Lodge, I want to provide my customers with information on the town and area attractions. I want to provide rate information. Ideally, I would like to have a button/page for each section: Welcome & Information, Area Attractions, Welcome to Leeds, Rates, Who's Tilda?!, FAQ's and Where are we?. I don't know if this would be more expensive the more pages you have? If more pages is too expensive, then we can combine info on less pages. I want my logo included on the web page. I want Mockup Meadow to take down my old website and use the same address to put up my newly designed website.

Target Market(s)

Full time RVers, People who camp, hunt fish, People who recreate on Devils Lake, People who are looking for meeting/conference space, people who are looking for party venue

Industry/Entity Type

Accommodation

Number of Pages Required

3 page

Requirements
Must have
• I want a cozy, welcoming type web site. No super dark colors. Bright and cheerful.
• Must be simple and organized.
• NOTE: I have a file of pictures of the interior of Tilda's Lodge that must be included in website. Please request this file if you will be designing my project as the files are too large to upload through Mockup Meadow.
Nice to have
• If you cannot open any of the files listed, please notify me.
Should not have
• No stark or super-formal designs.

```html
<!DOCTYPE html>
<html lang="en">
<head>
<meta charset="utf-8">
<title>Tilda's RV Park &amp; Lodge – Leeds, North Dakota</title>
<link href="https://fonts.googleapis.com/css2?family=Lato:wght@400;700;900&family=Open+Sans:wght@400;600;700&display=swap" rel="stylesheet">
<style>
:root{
  --maroon:#6a1a20;
  --maroon-deep:#4e1015;
  --green:#4b5f24;
  --green-deep:#34451a;
  --olive:#55682a;
  --grey-bg:#ececec;
  --text:#3a3a3a;
  --white:#ffffff;
}
*{margin:0;padding:0;box-sizing:border-box}
html,body{width:1200px;height:3327px;overflow:hidden}
body{position:relative;font-family:'Open Sans',sans-serif;color:var(--text);background:var(--white)}
.abs{position:absolute}

/* Header & hero */
.hero{left:0;top:0;width:1200px;height:700px;background:linear-gradient(180deg,#c9d6df 0%,#dfe4e4 30%,#a8a39a 55%,#8c8a6c 68%,#6e7f3c 82%,#5f7434 100%)}
.logo{left:0;top:0;width:260px;height:170px;background:rgba(255,255,255,.92);display:flex;flex-direction:column;align-items:center;justify-content:center;gap:8px}
.logo-mark{width:34px;height:34px;background:var(--green)}
.logo-name{font-family:'Lato',sans-serif;font-weight:700;font-size:17px;color:var(--maroon);text-align:center;line-height:1.2;width:180px}
.phone{right:60px;top:18px;font-family:'Lato',sans-serif;font-weight:700;font-size:22px;color:var(--maroon-deep);display:flex;align-items:center;gap:10px}
.navbar{left:288px;top:66px;width:912px;height:50px;background:linear-gradient(180deg,var(--olive),var(--green-deep));display:flex;align-items:center;padding-left:4px}
.navbar::before{content:"";position:absolute;left:-30px;top:0;border-style:solid;border-width:0 30px 50px 0;border-color:transparent var(--olive) transparent transparent}
.navbar a{font-family:'Lato',sans-serif;font-weight:700;font-size:15px;color:var(--white);text-decoration:none;margin:0 11px}
.hero-title{left:0;top:286px;width:1200px;text-align:center;font-family:'Lato',sans-serif;font-weight:900;font-size:38px;line-height:1.05;color:var(--white);text-transform:uppercase;text-shadow:0 2px 6px rgba(0,0,0,.55)}
.dots{left:560px;top:572px;display:flex;gap:8px}
.dots span{width:15px;height:15px;border-radius:50%;background:var(--white)}
.dots span:first-child{background:transparent;border:2px solid var(--white)}

/* Welcome */
.welcome{left:0;top:700px;width:1200px;text-align:center}
.welcome-mark{width:26px;height:26px;border-radius:50%;background:var(--maroon);margin:-50px auto 22px}
.welcome h1{font-family:'Lato',sans-serif;font-weight:900;font-size:30px;line-height:1.15;color:var(--maroon)}
.welcome p{width:840px;margin:24px auto 0;font-size:20px;line-height:1.55;color:var(--text)}

/* Lodge */
.lodge{left:0;top:910px;width:1200px;height:410px;background:var(--grey-bg)}
.circle-photo{border-radius:50%;border:4px solid var(--white);box-shadow:0 0 0 3px var(--maroon)}
.lodge .circle-photo{left:133px;top:88px;width:288px;height:288px;background:radial-gradient(circle at 45% 55%,#24408a 0%,#2f4a80 35%,#6c8ab0 70%,#a9c1da 100%)}
.lodge h2{left:453px;top:114px;font-family:'Lato',sans-serif;font-weight:900;font-size:24px;color:var(--green)}
.lodge p{left:453px;top:166px;width:615px;font-size:12.5px;line-height:1.42}

/* Meeting */
.meeting{left:0;top:1320px;width:1200px;height:410px;background:linear-gradient(180deg,var(--maroon) 0%,#58321e 55%,var(--green) 100%);color:var(--white)}
.meeting h2{left:142px;top:100px;font-family:'Lato',sans-serif;font-weight:700;font-size:26px}
.meeting p{left:142px;top:150px;width:590px;font-size:14.5px;line-height:1.65}
.meeting .circle-photo{left:760px;top:56px;width:286px;height:286px;background:radial-gradient(circle at 50% 55%,#e8e2d6 0%,#b8b2a6 45%,#6f6a66 80%,#4a4644 100%);border-color:var(--white);box-shadow:0 0 0 3px #d9cfc4}

/* Features */
.features{left:0;top:1730px;width:1200px;height:300px;background:var(--white)}
.features h2{left:0;top:40px;width:1200px;text-align:center;font-family:'Lato',sans-serif;font-weight:900;font-size:28px;color:var(--green)}
.feature{top:105px;width:200px;text-align:center;font-family:'Lato',sans-serif;font-weight:700;font-size:16px;line-height:1.4;color:#2c2c2c}
.feature svg{display:block;margin:0 auto 14px}
.slider-arrow{top:152px;width:40px;height:40px;border-radius:50%;border:2px solid #9a9a9a;display:flex;align-items:center;justify-content:center}

/* RV Park */
.rvpark{left:0;top:2007px;width:1200px;height:720px;background:linear-gradient(170deg,#7e272b 0%,var(--maroon) 45%,var(--maroon-deep) 100%);color:var(--white);text-align:center}
.rvpark h2{margin-top:98px;font-family:'Lato',sans-serif;font-weight:700;font-size:28px}
.rvpark .intro{width:880px;margin:18px auto 0;font-size:14px;line-height:1.72}
.rv-list{list-style:none;margin-top:22px;font-size:15px;line-height:29px}
.rv-list li::before{content:"›";font-weight:700;font-size:22px;margin-right:6px;line-height:0}
.rvpark h3{margin-top:22px;font-family:'Lato',sans-serif;font-weight:700;font-size:30px}
.rvpark .tents{font-weight:700;font-size:17px;margin-top:2px}

/* Rates */
.rates{left:0;top:2724px;width:1200px;height:428px}
.rates-bg{left:0;top:0;width:1200px;height:428px;background:linear-gradient(180deg,#5b7fae 0%,#8ca6c3 25%,#b9b7a4 45%,#3f5a22 65%,#5c7d2a 100%)}
.rates h2{left:0;top:26px;width:1200px;text-align:center;font-family:'Lato',sans-serif;font-weight:900;font-size:32px;color:var(--white)}
.rate-card{top:88px;width:318px;height:246px;background:var(--white);border:1px solid #d8d8d8;text-align:center;padding:30px 24px 0}
.rate-card h3{font-family:'Lato',sans-serif;font-weight:700;font-size:21px;color:var(--maroon);margin-bottom:22px}
.rate-card .price{font-family:'Lato',sans-serif;font-weight:700;font-size:18px;color:var(--green);line-height:1.3}
.rate-card p{font-size:13px;line-height:1.5;color:#444}
.rate-card.narrow p{padding:0 14px}
.rates .note{left:0;top:376px;width:1200px;text-align:center;font-size:16px;color:var(--white)}

/* Footer */
.footer{left:0;top:3150px;width:1200px;height:177px;background:linear-gradient(180deg,var(--green-deep),#2f3d17);color:var(--white);text-align:center}
.footer nav{margin-top:36px}
.footer nav a{font-family:'Lato',sans-serif;font-weight:700;font-size:15px;color:var(--white);text-decoration:none;margin:0 8px}
.footer .copy{font-size:12px;margin-top:8px}
.social{display:flex;justify-content:center;gap:10px;margin-top:22px}
.social span{width:34px;height:34px;border-radius:50%;border:2px solid var(--white)}
</style>
</head>
<body>

<div class="abs hero" role="img" aria-label="Photo of the lodge building on a grassy lot under a cloudy sky"></div>
<div class="abs logo">
  <div class="logo-mark"></div>
  <div class="logo-name">Tilda's RV Park &amp; Lodge<br>Leeds ND</div>
</div>
<div class="abs phone">
  <svg width="22" height="22" viewBox="0 0 24 24"><rect width="24" height="24" rx="3" fill="#4e1015"/><path d="M8 5l2 3-1.5 1.5a9 9 0 0 0 6 6L16 14l3 2-1 3c-6 0-13-7-13-13z" fill="#fff"/></svg>
  701-555-0187
</div>
<nav class="abs navbar">
  <a href="#">Home</a><a href="#">Welcome &amp; Information</a><a href="#">Area Attractions</a><a href="#">Welcome to Leeds</a><a href="#">Rates</a><a href="#">Who's Tilda?!</a><a href="#">FAQ's</a><a href="#">Where are we</a>
</nav>
<h1 class="abs hero-title">Heart of some of the greatest hunting<br>and fishing in the world</h1>
<div class="abs dots"><span></span><span></span><span></span><span></span></div>

<svg class="abs" style="left:0;top:600px" width="1200" height="120" viewBox="0 0 1200 120" preserveAspectRatio="none">
  <path d="M0 120 L0 60 Q600 -20 1200 60 L1200 120 Z" fill="#fff"/>
  <path d="M0 60 Q600 -20 1200 60" fill="none" stroke="#6a1a20" stroke-width="5"/>
</svg>

<section class="abs welcome">
  <div class="welcome-mark"></div>
  <h1>Welcome to Tilda's RV Park &amp; Lodge<br>and Leeds, North Dakota</h1>
  <p>Leeds is in the heart of some of the greatest hunting and fishing in the world. Tilda's RV Park is located right on Highway 2 midway between Devils Lake and Rugby North Dakota. We are smack dab in the middle of it all!</p>
</section>

<section class="abs lodge">
  <div class="abs circle-photo" role="img" aria-label="Photo of a large blue farm tractor"></div>
  <h2 class="abs">Tilda's Lodge</h2>
  <p class="abs">Are you looking for a cozy, but spacious home away from home? Well, you have found it! Tilda's Lodge is 2200 square feet of living space. There are 2 spacious bedrooms with queen sized beds and another common sleeping area with 5 sets of bunk beds. Available to you are 2 restrooms with showers, a great room with dining and relaxing space and a full kitchen. Everything is supplied for you: towels, bedding, cookware, dishware, grill and etc...all that you need to make your stay worry and hassle free. Throw some clothes in a suitcase, hit the road and we will have your home away from home all ready when you get here! The Lodge is open all year round.</p>
</section>
<svg class="abs" style="left:0;top:890px" width="1200" height="70" viewBox="0 0 1200 70" preserveAspectRatio="none">
  <path d="M0 0 L1200 0 L1200 20 Q600 70 0 20 Z" fill="#fff"/>
  <path d="M0 22 Q600 74 1200 22" fill="none" stroke="#4b5f24" stroke-width="5"/>
</svg>

<section class="abs meeting">
  <h2 class="abs">Meeting / Conference Space</h2>
  <p class="abs">Are you looking for a venue for your next meeting, training event, guys/girls weekend, quilt retreat, holiday gathering, family reunion, birthday, wedding party or get-together? We've got you covered! Tilda's Lodge seats about 65 people comfortably. Many of our customers have commented that Tilda's was the perfect place for their event because it was so inviting...and just like home!</p>
  <div class="abs circle-photo" role="img" aria-label="Photo of the lodge great room set with long tables and chairs for an event"></div>
</section>

<section class="abs features">
  <h2 class="abs">TILDA'S LODGE</h2>
  <div class="abs slider-arrow" style="left:80px"><svg width="14" height="14" viewBox="0 0 14 14"><path d="M9 2L4 7l5 5" fill="none" stroke="#777" stroke-width="2"/></svg></div>
  <div class="abs feature" style="left:114px">
    <svg width="74" height="74" viewBox="0 0 74 74"><circle cx="37" cy="37" r="34" fill="none" stroke="#6a1a20" stroke-width="3"/><circle cx="37" cy="37" r="15" fill="none" stroke="#6a1a20" stroke-width="3"/><path d="M37 14v46M14 37h46" stroke="#6a1a20" stroke-width="3"/></svg>
    Groups – hunting,<br>fishing, working, playing
  </div>
  <div class="abs feature" style="left:319px">
    <svg width="74" height="74" viewBox="0 0 74 74"><circle cx="37" cy="37" r="34" fill="none" stroke="#6a1a20" stroke-width="3"/><rect x="20" y="20" width="34" height="34" fill="none" stroke="#6a1a20" stroke-width="3"/><path d="M20 36h16v18M36 20v8M44 36h10" stroke="#6a1a20" stroke-width="2.5" fill="none"/></svg>
    2200<br>Square feet
  </div>
  <div class="abs feature" style="left:502px">
    <svg width="74" height="74" viewBox="0 0 74 74"><circle cx="37" cy="37" r="34" fill="none" stroke="#6a1a20" stroke-width="3"/><path d="M20 44h34v6H20zM26 44V30h22v14" fill="none" stroke="#6a1a20" stroke-width="3"/><path d="M30 26v-4M37 26v-4M44 26v-4" stroke="#6a1a20" stroke-width="2.5"/></svg>
    Full kitchen
  </div>
  <div class="abs feature" style="left:692px">
    <svg width="74" height="74" viewBox="0 0 74 74"><circle cx="37" cy="37" r="34" fill="none" stroke="#6a1a20" stroke-width="3"/><path d="M18 32a27 27 0 0 1 38 0M23 38a19 19 0 0 1 28 0M28 44a11 11 0 0 1 18 0" fill="none" stroke="#6a1a20" stroke-width="3.5" stroke-linecap="round"/><circle cx="37" cy="51" r="3.5" fill="#6a1a20"/></svg>
    Free WiFi
  </div>
  <div class="abs feature" style="left:876px">
    <svg width="74" height="74" viewBox="0 0 74 74"><circle cx="37" cy="37" r="34" fill="none" stroke="#6a1a20" stroke-width="3"/><path d="M22 30a16 16 0 0 0 22 22z" fill="#6a1a20"/><path d="M34 40l10-10M44 22a8 8 0 0 1 8 8M44 16a14 14 0 0 1 14 14" fill="none" stroke="#6a1a20" stroke-width="3"/><path d="M30 50l-4 8h14" stroke="#6a1a20" stroke-width="3" fill="none"/></svg>
    Satellite TV
  </div>
  <div class="abs slider-arrow" style="left:1085px"><svg width="14" height="14" viewBox="0 0 14 14"><path d="M5 2l5 5-5 5" fill="none" stroke="#777" stroke-width="2"/></svg></div>
</section>

<section class="abs rvpark">
  <h2>Tilda's RV PARK</h2>
  <p class="intro">Tilda's RV Park sits right next to Highway 2 on the north side. We have 14 full service spaces – sewer, water and electric (20, 30, 50 amp). There is an indoor restroom with shower that is available 24 hours a day to our RV customers. Plenty of space is available to you for parking boats, trailers, etc. Tilda's RV Park year round, but water usage depends on when spring thaw and freeze up occurs. Please note: Tilda's RV Park is an unattended RV park. No reservations required. Please pull on in, use our self-service check-in and then sit back and relax!</p>
  <ul class="rv-list">
    <li>14 Full Service Sites</li>
    <li>Electric (23, 30 &amp; 50amp), Water, Sewer</li>
    <li>Free WiFi</li>
    <li>Safe &amp; convenient location</li>
    <li>24 hour indoor restroom with shower</li>
    <li>Roamers Club accepted for first night</li>
    <li>Ample room to park boats, trailers etc.</li>
    <li>Convenience store/gas station located right across the street. Restaurant onsite.</li>
    <li>Tilda's operates on a first come, first serve basis for short term stays. If you would like to<br>reserve for a stay longer than 3 days, please call Tilda.</li>
  </ul>
  <h3>TENTS</h3>
  <p class="tents">Primitive &amp; tent sites are also available</p>
</section>
<svg class="abs" style="left:0;top:2000px" width="1200" height="70" viewBox="0 0 1200 70" preserveAspectRatio="none">
  <path d="M0 0 L1200 0 L1200 8 Q600 70 0 8 Z" fill="#fff"/>
</svg>

<section class="abs rates">
  <div class="abs rates-bg" role="img" aria-label="Photo of the green park lawn with trees under a blue sky"></div>
  <h2 class="abs">RATES</h2>
  <div class="abs rate-card" style="left:118px">
    <h3>Tilda's Lodge Pricing</h3>
    <div class="price">$200 for 24 hours.</div>
    <p>The first 6 adults are included in the $200 per night rent. Each adult exceeding the initial 6, must pay $25 per night. Kids under age 16 stay free.</p>
  </div>
  <div class="abs rate-card" style="left:448px">
    <h3>Tilda's RV Park Pricing</h3>
    <div class="price">RV Sites:<br>$24/Night $125/Week<br>$375/month</div>
    <p>This price is for 4 adults. Any adults exceeding the initial 4, must pay $5 extra per night. Kids under 16 stay free.</p>
  </div>
  <div class="abs rate-card narrow" style="left:774px">
    <h3>Showers</h3>
    <p>Showers are $5 per person for unregistered customers. There is no charge for anyone that uses the shower that is staying at Tilda's RV Park &amp; Lodge.</p>
  </div>
  <p class="abs note">Roamers Club accepted for the first night.</p>
</section>

<footer class="abs footer">
  <nav>
    <a href="#">Home</a><a href="#">Welcome &amp; Information</a><a href="#">Area Attractions</a><a href="#">Welcome to Leeds</a><a href="#">Rates</a><a href="#">Who's Tilda?!</a><a href="#">FAQ's</a><a href="#">Where are we</a>
  </nav>
  <p class="copy">© 2018 Company Name All right reserved Terms of Use</p>
  <div class="social"><span></span><span></span><span></span><span></span></div>
</footer>

</body>
</html>
```